Business card design for strategy and management consulting company. Would like to have a clean and professional business card, based on the attached logo. The company is a strategy and management consulting company focusing on sustainable business modlels based on economic, social and environmental market opportunities. Preferably the logo should be included on both sides of the design.

Industry/Entity Type

Business

Contact Information for Business Card

Håvard Lilleby, CEO/Management consultant
havard.lilleby@quarvenpartners.example
Mob: +47 948 26 317
Office: Vikfjell gate 14, pb 312 sentrum, N-0172 Oslo Norway

Requirements
Must have
• Include attached logo
Nice to have
• Would like to have the logo on both sides
Should not have
• Many colours.

```html
<!DOCTYPE html>
<html lang="en">
<head>
<meta charset="utf-8">
<title>Quarven – Business Card</title>
<link href="https://fonts.googleapis.com/css2?family=Oswald:wght@300;400;600&display=swap" rel="stylesheet">
<style>
  :root {
    --backdrop: #2b2e33;
    --paper: #f2f2f1;
    --ink: #1c1c1c;
    --ink-soft: #3a3a3a;
    --rule: #8a8a8a;
    --card-black: #141414;
    --card-black-edge: #262626;
    --logo-light: #ffffff;
  }
  * { box-sizing: border-box; margin: 0; padding: 0; }
  html, body {
    width: 1200px;
    height: 1000px;
    overflow: hidden;
    background: var(--backdrop);
    font-family: "Oswald", "Arial Narrow", sans-serif;
  }
  .stage {
    width: 1200px;
    height: 1000px;
    display: flex;
    flex-direction: column;
    align-items: center;
    justify-content: center;
    gap: 60px;
  }
  .card {
    width: 700px;
    height: 400px;
    border-radius: 30px;
    position: relative;
    overflow: hidden;
  }

  /* Front */
  .card--front {
    background: var(--paper);
    color: var(--ink);
    display: flex;
    flex-direction: column;
    align-items: center;
    padding-top: 62px;
  }
  .brand-name {
    font-family: "Oswald", "Arial Narrow", sans-serif;
    font-weight: 400;
    letter-spacing: 1px;
    line-height: 1;
  }
  .card--front .brand-name {
    font-size: 58px;
    color: var(--ink);
  }
  .details {
    margin-top: 44px;
    display: flex;
    align-items: stretch;
  }
  .person {
    text-align: right;
    padding-right: 20px;
    text-transform: uppercase;
  }
  .person__first {
    font-weight: 300;
    font-size: 30px;
    line-height: 1;
    letter-spacing: 2px;
    color: var(--ink-soft);
  }
  .person__last {
    font-weight: 600;
    font-size: 50px;
    line-height: 1;
    letter-spacing: 1px;
  }
  .person__role {
    margin-top: 6px;
    font-weight: 400;
    font-size: 11.5px;
    letter-spacing: 0.6px;
  }
  .divider {
    width: 1px;
    background: var(--rule);
  }
  .contact {
    padding-left: 20px;
    display: flex;
    flex-direction: column;
    justify-content: center;
    gap: 5px;
    font-size: 13px;
    font-weight: 400;
    letter-spacing: 0.8px;
    text-transform: uppercase;
    color: var(--ink-soft);
  }
  .contact__address { line-height: 1.35; margin-bottom: 4px; }
  .contact__line { display: flex; align-items: center; gap: 7px; }
  .contact__icon { width: 12px; height: 12px; flex: none; }

  /* Back */
  .card--back {
    background: radial-gradient(ellipse at 40% 30%, var(--card-black-edge), var(--card-black) 70%);
    display: flex;
    align-items: center;
    justify-content: center;
  }
  .card--back .brand-name {
    font-size: 110px;
    color: var(--logo-light);
  }
</style>
</head>
<body>
  <main class="stage">
    <section class="card card--front" aria-label="Business card front">
      <div class="brand-name">Quarven</div>
      <div class="details">
        <div class="person">
          <div class="person__first">Håvard</div>
          <div class="person__last">Lilleby</div>
          <div class="person__role">CEO/Management Consultant</div>
        </div>
        <div class="divider"></div>
        <div class="contact">
          <div class="contact__address">Vikfjell gate 14, pb 312<br>sentrum, N-0172 Oslo Norway</div>
          <div class="contact__line">
            <svg class="contact__icon" viewBox="0 0 24 24" aria-hidden="true">
              <path fill="currentColor" d="M6.6 10.8c1.4 2.8 3.8 5.1 6.6 6.6l2.2-2.2c.3-.3.7-.4 1-.2 1.1.4 2.3.6 3.6.6.6 0 1 .4 1 1V20c0 .6-.4 1-1 1C10.6 21 3 13.4 3 4c0-.6.4-1 1-1h3.5c.6 0 1 .4 1 1 0 1.3.2 2.5.6 3.6.1.3 0 .7-.2 1l-2.3 2.2z"/>
            </svg>
            <span>+47 948 26 317</span>
          </div>
          <div class="contact__line">
            <svg class="contact__icon" viewBox="0 0 24 24" aria-hidden="true">
              <rect x="2" y="5" width="20" height="14" rx="1.5" fill="none" stroke="currentColor" stroke-width="2"/>
              <path d="M3 6l9 7 9-7" fill="none" stroke="currentColor" stroke-width="2"/>
            </svg>
            <span>havard.lilleby@quarvenpartners.example</span>
          </div>
        </div>
      </div>
    </section>

    <section class="card card--back" aria-label="Business card back">
      <div class="brand-name">Quarven</div>
    </section>
  </main>
</body>
</html>
```